Pages toward Inner Calm - book cover

12/18 update: Please read the entire brief. I don’t love anything that has been provided up to today. Please use the graphics and colors I’ve attached!!!! Show me your creations.

I am looking for a book cover design. It is a mental health journal. Needs to be very warm, inviting, calming. I’m very interested in new creative ideas. It will be wire-o bound and also in hard copy front and back. Use the graphic and colors I already have attached to this file. It’s called “Pages Toward Inner Calm”. Self means soul or spirit or center. The idea of integration may be a fit here in some way. If some words need to be emphasized in the design, “Self” and “QRM” would be the most important. size 6"x9". The words on the front can be smaller and more inviting then they would normally be on a fiction paperback.

Update 12/16: I am not excited about any of the submissions so far. I’m looking forward to seeing more options.

Target Market(s)

Adults 30-60. Male and female. People who like to learn. People wanting to heal. Middle and upper income.

Industry/Entity Type

Mental health. Wellness

Font styles to use
Other font styles liked:
• Whatever font is used in my logo. i don’t know the name. I also would be open to a different font if it was warm, inviting, and calm.

Colors
0094D4
00A9DD
6FCCEA
C7EBF8
E9F6FB

Requirements
Must have
• My logo colors. The words “Pages Toward Inner Calm” and “A 13-Week QRM Exploration”
Nice to have
• I’d like to see some creative ideas. More abstract than realistic.
Should not have
• No realist art or photos.

```html
<!DOCTYPE html>
<html lang="en">
<head>
<meta charset="UTF-8">
<title>Pages toward Inner Calm – Book Cover</title>
<link href="https://fonts.googleapis.com/css2?family=Cinzel:wght@500;600&family=EB+Garamond:wght@500&display=swap" rel="stylesheet">
<style>
  :root {
    --page-bg: #ffffff;
    --cover-bg: #fbfaf5;
    --teal: #179294;
    --ink: #111111;
    --band: #175568;
    --band-text: #ffffff;
    --art-teal: #6fcfc9;
    --art-pink: #e9779b;
    --art-purple: #5b4aa8;
    --art-coral: #d9625a;
  }
  * { margin: 0; padding: 0; box-sizing: border-box; }
  html, body {
    width: 1200px; height: 1200px; overflow: hidden;
    background: var(--page-bg);
  }
  .cover {
    position: absolute;
    left: 258px; top: 88px;
    width: 684px; height: 1025px;
    background: var(--cover-bg);
    overflow: hidden;
  }
  .title {
    position: absolute; top: 52px; left: 0; width: 100%;
    text-align: center;
  }
  .title-main {
    font-family: "Cinzel", serif;
    font-weight: 500;
    color: var(--teal);
    line-height: 1;
    display: block;
  }
  .title-top { font-size: 122px; letter-spacing: -2px; }
  .title-bottom { font-size: 178px; letter-spacing: -4px; margin-top: -4px; }
  .title-link {
    display: flex; align-items: center; justify-content: center;
    gap: 14px; width: 500px; margin: 4px auto 0;
  }
  .title-link .rule {
    flex: 1; height: 2px; background: var(--ink);
    border-radius: 2px;
  }
  .title-link span {
    font-family: "EB Garamond", serif; font-weight: 500;
    font-size: 44px; color: var(--ink); line-height: 1;
    white-space: nowrap;
  }
  .subtitle {
    position: absolute; top: 428px; left: 0; width: 100%;
    text-align: center;
    font-family: "EB Garamond", serif; font-weight: 500;
    font-size: 36px; color: var(--ink); line-height: 1;
    white-space: nowrap;
  }
  .subtitle .emphasis {
    font-family: "Cinzel", serif; font-weight: 600;
    color: var(--teal); font-size: 44px;
  }
  .art {
    position: absolute; top: 497px; left: 0;
    width: 684px; height: 453px; display: block;
  }
  .author-band {
    position: absolute; left: 0; bottom: 0;
    width: 100%; height: 75px;
    background: var(--band);
    display: flex; align-items: center; justify-content: center;
  }
  .author-band span {
    font-family: "EB Garamond", serif; font-weight: 500;
    font-size: 34px; letter-spacing: 19px; color: var(--band-text);
    padding-left: 19px;
  }
</style>
</head>
<body>
  <div class="cover">
    <h1 class="title">
      <span class="title-main title-top">PAGES</span>
      <span class="title-link"><i class="rule"></i><span>TOWARD INNER</span><i class="rule"></i></span>
      <span class="title-main title-bottom">CALM</span>
    </h1>
    <p class="subtitle">A 13-WEEK <span class="emphasis">QRM</span> EXPLORATION</p>

    <svg class="art" viewBox="0 0 684 453" role="img" aria-label="Abstract watercolour illustration: a profile silhouette filled with mountains and a tree, colour drifting away in teal, pink and violet splashes, a small figure standing at its base">
      <defs>
        <radialGradient id="wash-teal" cx="0.62" cy="0.28" r="0.35">
          <stop offset="0" stop-color="var(--art-teal)" stop-opacity="0.75"/>
          <stop offset="1" stop-color="var(--art-teal)" stop-opacity="0"/>
        </radialGradient>
        <radialGradient id="wash-pink" cx="0.4" cy="0.55" r="0.4">
          <stop offset="0" stop-color="var(--art-pink)" stop-opacity="0.6"/>
          <stop offset="1" stop-color="var(--art-pink)" stop-opacity="0"/>
        </radialGradient>
        <radialGradient id="wash-purple" cx="0.5" cy="0.95" r="0.4">
          <stop offset="0" stop-color="var(--art-purple)" stop-opacity="0.55"/>
          <stop offset="1" stop-color="var(--art-purple)" stop-opacity="0"/>
        </radialGradient>
        <radialGradient id="wash-coral" cx="0.75" cy="0.9" r="0.35">
          <stop offset="0" stop-color="var(--art-coral)" stop-opacity="0.55"/>
          <stop offset="1" stop-color="var(--art-coral)" stop-opacity="0"/>
        </radialGradient>
      </defs>
      <rect width="684" height="453" fill="var(--cover-bg)"/>
      <rect width="684" height="453" fill="url(#wash-teal)"/>
      <rect width="684" height="453" fill="url(#wash-pink)"/>
      <rect width="684" height="453" fill="url(#wash-purple)"/>
      <rect width="684" height="453" fill="url(#wash-coral)"/>
    </svg>

    <div class="author-band"><span>AUTHOR NAME</span></div>
  </div>
</body>
</html>
```